Income Tax Flyer - Updates Needed

Just need to update this flyer design and give it a new look. We would like to keep all the same wording but make it stand out a little more. Our selling point is the "Same Day Tax Advance up to $6,000"

Industry/Entity Type

Lending, Small Loans, Tax Services, Title Loans, Personal Loans

```html
<!DOCTYPE html>
<html lang="en">
<head>
<meta charset="utf-8">
<title>Same Day Tax Advance Flyer</title>
<link href="https://fonts.googleapis.com/css2?family=Poppins:wght@400;500;600;700;800&display=swap" rel="stylesheet">
<style>
  :root {
    --green: #0f5a2f;
    --red: #d42229;
    --gray: #4a4a4a;
    --white: #ffffff;
    --paper: #f6f6f6;
    --backdrop: #e8e8e8;
  }
  * { box-sizing: border-box; margin: 0; padding: 0; }
  html, body { width: 1200px; height: 3621px; overflow: hidden; }
  body { background: var(--backdrop); font-family: "Poppins", sans-serif; position: relative; }

  .flyer {
    position: absolute; left: 100px; top: 1102px;
    width: 1000px; height: 1416px;
    background: var(--paper); overflow: hidden;
    box-shadow: 0 20px 50px rgba(0,0,0,.18);
  }
  .flyer__photo {
    position: absolute; inset: 0 0 auto 0; height: 780px;
    background: linear-gradient(120deg, #d9dde2 0%, #c9b7a3 35%, #e4e6ea 55%, #6b5446 80%, #cfd3d8 100%);
  }
  .flyer__shapes { position: absolute; inset: 0; }

  .brand {
    position: absolute; left: 369px; top: 464px; width: 264px; height: 145px;
    background: var(--white); border-radius: 12px;
    box-shadow: 0 4px 14px rgba(0,0,0,.15);
    display: flex; align-items: center; justify-content: center; gap: 10px;
  }
  .brand__dot { width: 18px; height: 18px; border-radius: 50%; background: var(--green); }
  .brand__name { color: var(--green); font-weight: 600; font-size: 26px; line-height: 1.1; text-align: center; }

  .headline { position: absolute; left: 0; right: 0; text-align: center; font-weight: 800; letter-spacing: 1px; }
  .headline--main { top: 668px; font-size: 122px; line-height: 1; color: var(--green); padding-left: 70px; }
  .headline--sub { top: 792px; font-size: 92px; line-height: 1; color: var(--gray); padding-left: 90px; }

  .amount {
    position: absolute; left: 223px; top: 899px; width: 555px; height: 82px;
    background: var(--red); border-radius: 10px; color: var(--white);
    display: flex; align-items: center; justify-content: center; gap: 14px;
    font-size: 56px; line-height: 1;
  }
  .amount__lead { font-weight: 400; }
  .amount__value { font-weight: 800; }

  .pitch { position: absolute; left: 0; right: 0; top: 1004px; text-align: center; line-height: 1.1; }
  .pitch__line { font-size: 50px; font-weight: 500; color: var(--green); }
  .pitch__accent { font-size: 54px; font-weight: 800; color: var(--red); }

  .features {
    position: absolute; left: 0; right: 0; top: 1150px; height: 147px;
    background: var(--green); display: flex; align-items: center; justify-content: space-around;
    padding: 0 30px 10px;
  }
  .feature { display: flex; align-items: center; gap: 18px; color: var(--white); font-size: 25px; line-height: 1.25; }
  .feature__icon {
    width: 80px; height: 80px; border-radius: 50%; background: var(--white);
    display: flex; align-items: center; justify-content: center; flex: none;
  }

  .cta {
    position: absolute; left: 352px; top: 1278px; width: 278px; height: 48px;
    background: var(--red); color: var(--white); font-weight: 700; font-size: 26px;
    display: flex; align-items: center; justify-content: center;
  }
  .contact {
    position: absolute; top: 1340px; display: flex; align-items: center; gap: 16px;
  }
  .contact--phone { left: 103px; font-size: 44px; font-weight: 800; color: var(--gray); }
  .contact--address { left: 590px; top: 1348px; font-size: 31px; font-weight: 400; color: var(--gray); letter-spacing: 3px; }
  .contact__icon { width: 32px; height: 32px; border-radius: 7px; background: var(--red); display: flex; align-items: center; justify-content: center; }
</style>
</head>
<body>
<main class="flyer">
  <div class="flyer__photo" role="img" aria-label="Photo of two smiling women in a bright office"></div>

  <svg class="flyer__shapes" viewBox="0 0 1000 1416" width="1000" height="1416" aria-hidden="true">
    <path d="M0,790 Q500,430 1000,700 L1000,1416 L0,1416 Z" fill="#f6f6f6"/>
    <path d="M0,770 Q380,500 700,500" fill="none" stroke="#d42229" stroke-width="14"/>
    <path d="M0,748 Q300,520 560,500" fill="none" stroke="#0f5a2f" stroke-width="14"/>
    <path d="M640,500 Q860,520 1000,660" fill="none" stroke="#0f5a2f" stroke-width="18"/>
    <path d="M600,520 Q820,550 960,700" fill="none" stroke="#d42229" stroke-width="5"/>
    <path d="M150,870 Q150,690 300,650" fill="none" stroke="#d42229" stroke-width="9" stroke-linecap="round"/>
    <path d="M290,628 L325,648 L292,670 Z" fill="#d42229"/>
  </svg>

  <div class="brand">
    <span class="brand__dot"></span>
    <span class="brand__name">Harbor Lane<br>Financial Group</span>
  </div>

  <h1 class="headline headline--main">SAME DAY</h1>
  <h2 class="headline headline--sub">TAX ADVANCE</h2>

  <div class="amount"><span class="amount__lead">UP TO</span><span class="amount__value">$6,000</span></div>

  <p class="pitch">
    <span class="pitch__line">File your taxes and apply for an</span><br>
    <span class="pitch__accent">Easy Advance!</span>
  </p>

  <section class="features">
    <div class="feature">
      <span class="feature__icon"><svg width="46" height="46" viewBox="0 0 46 46"><circle cx="23" cy="23" r="17" fill="none" stroke="#0f5a2f" stroke-width="3"/><path d="M23 12v11l8 5" fill="none" stroke="#d42229" stroke-width="3" stroke-linecap="round"/></svg></span>
      <span>Available In<br>24 Hours or Less</span>
    </div>
    <div class="feature">
      <span class="feature__icon"><svg width="46" height="46" viewBox="0 0 46 46"><circle cx="21" cy="21" r="12" fill="none" stroke="#0f5a2f" stroke-width="3"/><text x="21" y="27" font-size="15" font-weight="700" fill="#d42229" text-anchor="middle" font-family="Poppins, sans-serif">$</text><path d="M28 30l10 10" stroke="#0f5a2f" stroke-width="3" stroke-linecap="round"/></svg></span>
      <span>Choose Your<br>Loan Amount</span>
    </div>
    <div class="feature">
      <span class="feature__icon"><svg width="46" height="46" viewBox="0 0 46 46"><circle cx="27" cy="23" r="13" fill="none" stroke="#0f5a2f" stroke-width="3"/><text x="27" y="29" font-size="15" font-weight="700" fill="#d42229" text-anchor="middle" font-family="Poppins, sans-serif">$</text><path d="M3 17h9M1 23h10M3 29h9" stroke="#0f5a2f" stroke-width="3" stroke-linecap="round"/></svg></span>
      <span>Quick and<br>Easy</span>
    </div>
  </section>

  <div class="cta">Contact Us Today!</div>

  <div class="contact contact--phone">
    <span class="contact__icon"><svg width="20" height="20" viewBox="0 0 20 20"><path d="M5 2l3 4-2 2q2 4 6 6l2-2 4 3-2 3Q8 17 2 5Z" fill="#fff"/></svg></span>
    <span>Phone Number</span>
  </div>
  <div class="contact contact--address">
    <span class="contact__icon"><svg width="20" height="20" viewBox="0 0 20 20"><path d="M10 2a6 6 0 0 1 6 6c0 4-6 10-6 10S4 12 4 8a6 6 0 0 1 6-6Z" fill="#fff"/><circle cx="10" cy="8" r="2" fill="#d42229"/></svg></span>
    <span>Address line 1</span>
  </div>
</main>
</body>
</html>
```